Brackenvale.com Postcard

We want to create a postcard, which is going to be mailed out to 6k managers at Hospitals throughout the USA.

I attached a rough draft of what I want the postcard to look like, but want it to look much better. The postcard size is 5.47" * 4.21"

```html
<!DOCTYPE html>
<html lang="en">
<head>
<meta charset="utf-8">
<title>Brackenvale Medical Postcard</title>
<link rel="stylesheet" href="https://fonts.googleapis.com/css2?family=Fira+Sans:wght@400;600;700&family=Fira+Sans+Condensed:wght@300;400&display=swap">
<style>
  :root {
    --page: #e4e4e4;
    --navy: #1d3c73;
    --navy-deep: #162f5e;
    --navy-glow: #3f74bd;
    --white: #ffffff;
    --rule: rgba(255,255,255,0.55);
    --ghost: rgba(255,255,255,0.08);
    --arrow-blue: #2a8fc4;
    --arrow-purple: #5a4aa0;
    --arrow-orange: #e28a2c;
    --arrow-green: #4fb08f;
    --ink: #222222;
    --muted: #9a9a9a;
  }
  * { margin: 0; padding: 0; box-sizing: border-box; }
  html, body { width: 771px; height: 1200px; overflow: hidden; }
  body { background: var(--page); position: relative; font-family: "Fira Sans", sans-serif; color: var(--white); }

  .card {
    position: absolute; left: 27px; width: 714px;
    background: radial-gradient(ellipse at 50% 45%, var(--navy-glow) 0%, var(--navy) 55%, var(--navy-deep) 100%);
    box-shadow: 2px 3px 6px rgba(0,0,0,0.3);
    overflow: hidden;
  }
  .card--front { top: 33px; height: 553px; }
  .card--back { top: 611px; height: 554px; }

  .iv-decor { position: absolute; background: linear-gradient(180deg, var(--ghost), rgba(255,255,255,0.03)); border-radius: 6px; }
  .card--front .iv-decor { left: 10px; top: 10px; width: 130px; height: 480px; }
  .card--back .iv-decor { left: 8px; top: 180px; width: 90px; height: 370px; }

  .brand { position: absolute; text-align: center; }
  .brand__mark { display: block; margin: 0 auto; width: 30px; height: 30px; border-radius: 50%; background: var(--white); }
  .brand__rule { height: 1px; background: linear-gradient(90deg, transparent, var(--rule), transparent); }
  .brand__name { font-family: "Fira Sans", sans-serif; font-weight: 400; letter-spacing: 2px; font-size: 38px; line-height: 50px; }
  .card--front .brand { left: 20px; width: 674px; top: 28px; }
  .card--back .brand { left: 20px; width: 506px; top: 20px; }
  .brand .brand__rule:first-of-type { margin-top: 20px; }

  .headline { position: absolute; left: 0; width: 100%; top: 160px; text-align: center; font-weight: 600; font-size: 70px; line-height: 80px; text-shadow: 0 3px 4px rgba(0,0,0,0.35); }
  .lede { position: absolute; left: 0; width: 100%; text-align: center; font-family: "Fira Sans Condensed", sans-serif; }
  .lede--main { top: 254px; font-size: 20px; font-weight: 300; letter-spacing: 0.3px; }
  .lede--small { top: 284px; font-size: 14.5px; font-weight: 400; }

  .photo-strip { position: absolute; left: 33px; top: 325px; width: 648px; height: 90px; display: flex; gap: 3px; padding: 0; }
  .photo { flex: 1; background: linear-gradient(135deg, #c9d3dc, #7d8b99); }
  .photo:nth-child(2) { background: linear-gradient(135deg, #e5e9ea, #a4b3b9); }
  .photo:nth-child(3) { background: linear-gradient(135deg, #dfe4ee, #8fa0bd); }
  .photo:nth-child(4) { background: linear-gradient(135deg, #98a4b2, #3f4d66); }
  .photo:nth-child(5) { background: linear-gradient(135deg, #e3ece9, #7fb3b0); }

  .call { position: absolute; top: 442px; left: 0; width: 100%; text-align: center; font-family: "Fira Sans Condensed", sans-serif; font-weight: 400; font-size: 22px; }

  .contact-bar { position: absolute; left: 18px; top: 490px; width: 678px; height: 34px; }
  .contact-bar span { position: absolute; top: 0; height: 34px; line-height: 34px; text-align: center; font-family: "Fira Sans Condensed", sans-serif; font-size: 15px; }

  .postage-panel { position: absolute; left: 0; top: 0; }
  .postage-box { position: absolute; left: 559px; top: 34px; width: 131px; height: 124px; border: 1.5px solid #bdbdbd; color: var(--muted); font-size: 12px; text-align: center; padding-top: 38px; line-height: 17px; }
  .address-line { position: absolute; left: 393px; width: 280px; height: 1.5px; background: var(--ink); }

  .back-copy { position: absolute; left: 39px; top: 198px; width: 290px; }
  .back-copy__title { font-weight: 600; font-size: 34px; line-height: 44px; text-shadow: 0 2px 3px rgba(0,0,0,0.3); }
  .back-copy__details { margin-top: 8px; width: 292px; text-align: center; font-weight: 600; font-size: 15px; line-height: 20px; }
  .back-copy__site { font-size: 20px; line-height: 26px; }
  .back-copy__phone { font-size: 25px; line-height: 32px; margin-top: 2px; }
</style>
</head>
<body>

<section class="card card--front">
  <div class="iv-decor" role="img" aria-label="Faint IV pole and drip bags decoration"></div>
  <header class="brand">
    <span class="brand__mark"></span>
    <div class="brand__rule"></div>
    <div class="brand__name">Brackenvale Medical</div>
    <div class="brand__rule"></div>
  </header>
  <h1 class="headline">We Buy IV Pumps</h1>
  <p class="lede lede--main">Looking to sell your Infusion IV Pumps?&nbsp; We will purchase all quality pumps.</p>
  <p class="lede lede--small">We offer competitive pricing and will purchase from companies and individuals.</p>
  <div class="photo-strip">
    <div class="photo" role="img" aria-label="Photo of an infusion pump keypad"></div>
    <div class="photo" role="img" aria-label="Photo of a hand adjusting an IV pump"></div>
    <div class="photo" role="img" aria-label="Photo of a patient beside an infusion pump"></div>
    <div class="photo" role="img" aria-label="Photo of a nurse operating a pump"></div>
    <div class="photo" role="img" aria-label="Photo of stacked syringe pumps"></div>
  </div>
  <p class="call">Sell infusion pumps to Brackenvale Medical today!</p>
  <div class="contact-bar">
    <svg width="678" height="34" viewBox="0 0 678 34" aria-hidden="true">
      <polygon points="0,17 14,0 60,0 60,34 14,34" fill="var(--arrow-blue)"/>
      <polygon points="55,0 258,0 258,34 55,34 66,17" fill="var(--arrow-purple)"/>
      <polygon points="258,0 510,0 510,34 258,34" fill="var(--arrow-orange)"/>
      <polygon points="510,0 664,0 678,17 664,34 510,34 521,17" fill="var(--arrow-green)"/>
    </svg>
    <span style="left:60px;width:198px">555-204-7719</span>
    <span style="left:258px;width:252px">Sales@Brackenvale.com</span>
    <span style="left:515px;width:150px">Brackenvale.com</span>
  </div>
</section>

<section class="card card--back">
  <div class="iv-decor" role="img" aria-label="Faint IV pole and drip bags decoration"></div>
  <svg class="postage-panel" width="714" height="554" viewBox="0 0 714 554" aria-hidden="true">
    <polygon points="536,17 714,17 714,554 90,554 90,457 346,457 346,176 536,176" fill="var(--white)"/>
  </svg>
  <header class="brand">
    <span class="brand__mark"></span>
    <div class="brand__rule"></div>
    <div class="brand__name">Brackenvale Medical</div>
    <div class="brand__rule"></div>
  </header>
  <div class="postage-box">Postage<br>Area</div>
  <div class="address-line" style="top:294px"></div>
  <div class="address-line" style="top:332px"></div>
  <div class="address-line" style="top:369px"></div>
  <div class="back-copy">
    <h2 class="back-copy__title">We Buy IV Pumps!</h2>
    <div class="back-copy__details">
      <div class="back-copy__site">Brackenvale.com</div>
      <div>PO Box 3180</div>
      <div>Fernbrook, NC 27999</div>
      <div class="back-copy__phone">555-204-7719</div>
      <div>Fax: 888-555-0163</div>
      <div>Email: sales@brackenvale.com</div>
    </div>
  </div>
</section>

</body>
</html>
```